Ridgecrest Balusters Website Redesign

I want a fresh new design for my website. Original website
www.ridgecrestbalusters.example. Will need to add additional photos for winning designer. Please use the basic layout for new design. Looking to get a more modern, functional site to attract new customer and ne bale to highlight past projects. Need it to be easy to navigate and get in touch with me for inquiries.

Target Market(s)

Builders and home owners in WA state

Industry/Entity Type

Building, Construction, Deck building

Coding

Coded - Design and coding required

Number of Pages Required

5+ page

Font styles to use
Sans Serif

Colors
0054AA
0677BA
7BADD7
CADEEF
E8F1F8
0094D4
00A9DD
6FCCEA
C7EBF8
E9F6FB
00AB8E
00BBA5
67D7C9
C6EFE9
E9F9F6
59FF00
82FF00
B8FF75
E3FFCB
F4FFEA

Requirements
Must have
• Will need to add more photos of completed projects
Nice to have
• Fresh take on old website, something modern
Should not have
• Nothing comes to mind

```html
<!DOCTYPE html>
<html lang="en">
<head>
<meta charset="utf-8">
<title>Ridgecrest Balusters – Website Layouts</title>
<link href="https://fonts.googleapis.com/css2?family=Lato:wght@400;700;900&display=swap" rel="stylesheet">
<style>
:root{
  --green:#0b6b38;
  --blue:#0677BA;
  --blue-dark:#0054AA;
  --teal:#00AB8E;
  --teal-light:#1fb79b;
  --mint:#C6EFE9;
  --pale:#E8F1F8;
  --sky:#E9F6FB;
  --ink:#3c4650;
  --photo-dark:#4a5560;
  --photo-mid:#7d8a90;
  --bg-a:#0e4f5c;
  --bg-b:#86e3f2;
}
*{box-sizing:border-box;margin:0;padding:0}
html,body{width:1200px;height:1200px;overflow:hidden}
body{font-family:'Lato',sans-serif;color:var(--ink);
  background:radial-gradient(ellipse at 55% 35%,var(--bg-b) 0%,#3fb0c6 45%,var(--bg-a) 100%)}
.page{position:absolute;background:#fff;transform-origin:top left;overflow:hidden}
.desktop{width:500px;height:1895px;left:330px;top:12px;transform:scale(.622)}
.mobile{width:210px;height:1820px;left:690px;top:12px;transform:scale(.645)}
.block{position:relative;width:100%;overflow:hidden}
.photo{background:linear-gradient(160deg,var(--photo-mid),var(--photo-dark))}
.photo-light{background:linear-gradient(160deg,#c9d2d6,#8d999e)}
.brand{color:var(--green);font-weight:700;letter-spacing:.02em;line-height:1;display:flex;align-items:center;gap:5px}
.brand-mark{width:10px;height:10px;border:1.5px solid var(--green)}
.btn{display:inline-flex;align-items:center;gap:5px;background:var(--blue);color:#fff;font-weight:700;text-transform:uppercase;white-space:nowrap}
.btn svg{display:block}
h2.title{color:var(--blue);font-weight:700;text-transform:uppercase;text-align:center;line-height:1.2}
.center{text-align:center}
.abs{position:absolute}
/* desktop */
.d-top{height:16px;background:var(--green);color:#fff;font-size:6px;display:flex;justify-content:flex-end;align-items:center;gap:14px;padding-right:45px}
.d-nav{height:19px;display:flex;align-items:center;justify-content:space-between;padding:0 40px}
.d-nav .brand{font-size:7px}
.d-nav ul{display:flex;gap:9px;list-style:none;font-size:5.5px;color:var(--blue);font-weight:700;align-items:center}
.d-nav .btn{font-size:5.5px;padding:3px 8px}
.d-hero{height:250px;display:flex;flex-direction:column;align-items:center;justify-content:center;color:#fff;text-align:center}
.d-hero h1{font-size:20px;font-weight:900;line-height:1.22;text-transform:uppercase;max-width:390px}
.d-hero p{font-size:9px;margin:10px 0 8px;text-transform:uppercase}
.d-hero .btn{font-size:5.5px;padding:5px 7px}
.dots{display:flex;gap:4px;position:absolute;bottom:10px;left:50%;transform:translateX(-50%)}
.dots i{width:6px;height:6px;border-radius:50%;background:#fff}
.dots i:first-child{background:var(--blue)}
.d-intro{height:150px;padding-top:34px}
.d-intro h2{font-size:13px}
.d-intro p{font-size:5.3px;line-height:1.65;max-width:395px;margin:12px auto 10px;text-align:center}
.btn-row{display:flex;justify-content:center;gap:4px}
.d-intro .btn{font-size:5px;padding:4px 9px}
.d-products{height:197px}
.d-products h2{font-size:13px}
.d-products .sub{font-size:5.3px;margin:12px 0 8px}
.cards{display:flex;gap:4px;padding:0 40px}
.card{flex:1}
.card .img{height:106px}
.card .label{font-size:5.2px;color:var(--blue);font-weight:700;margin-top:4px;text-transform:uppercase}
.feature{background:var(--teal-light);color:#fff;padding:6px;position:relative;overflow:hidden}
.feature .inner{border:1px solid rgba(255,255,255,.6);height:100%;padding:12px 8px;overflow:hidden}
.feature b{font-size:4.8px;text-transform:uppercase;display:block;margin-bottom:4px}
.feature p{font-size:4.5px;line-height:1.5}
.feature .more{display:inline-block;background:var(--blue);font-size:4.2px;padding:2px 4px;margin-top:4px}
.d-process{height:269px}
.d-process .panel{position:absolute;left:0;top:35px;width:248px;height:200px;background:rgba(255,255,255,.82);padding:18px 0 0 40px}
.d-process h2{font-size:13px;text-align:left;color:var(--blue)}
.step{display:flex;gap:6px;margin-top:11px}
.step .ic{width:12px;height:12px;flex:none;border-radius:2px;background:var(--sky);display:flex;align-items:center;justify-content:center}
.step h4{font-size:7.5px;color:#2b95d2;font-weight:400}
.step p{font-size:5px;line-height:1.55;color:#555;max-width:170px;margin-top:2px}
.d-process .btn{position:absolute;left:283px;top:216px;font-size:5px;padding:4px 8px}
.d-why{height:280px;background:var(--pale);padding-top:33px}
.d-why h2{font-size:13px}
.why-item{position:absolute;width:108px}
.why-item h4{font-size:6px;color:var(--blue);font-weight:400}
.why-item p{font-size:4.6px;line-height:1.55;color:#555;margin-top:3px}
.why-item.r{text-align:right}
.why-ic{position:absolute;width:14px;height:14px;border-radius:50%;background:var(--blue)}
.d-show{height:330px;padding-top:35px}
.d-show h2{font-size:13px}
.grid{display:grid;grid-template-columns:repeat(3,1fr);grid-auto-rows:101px;gap:6px;padding:0 40px;margin-top:16px}
.d-show .btn{font-size:5px;padding:4px 9px}
.d-test{height:185px}
.d-test h2{font-size:12px}
.d-stats{height:120px;display:flex;gap:6px;padding:0 40px}
.stat{flex:1;background:var(--mint);height:80px;text-align:center;color:var(--green);padding-top:6px;text-transform:uppercase}
.stat .big{font-size:26px;font-weight:400;line-height:1}
.stat small{display:block;font-size:5px;line-height:1.3}
.stat b{display:block;font-size:9px;margin-top:4px}
.d-foot{height:78px;background:var(--green);color:#fff;position:absolute;bottom:0;left:0;width:100%;font-size:4.6px}
.d-foot h5{font-size:6px;font-weight:400;margin-bottom:4px}
.d-foot li{list-style:none;line-height:2}
/* mobile */
.m-head{height:31px;background:var(--mint);display:flex;align-items:center;justify-content:space-between;padding:0 8px}
.m-head .brand{font-size:6.5px}
.burger{width:12px;height:7px;border-top:1px solid var(--green);border-bottom:1px solid var(--green);position:relative}
.burger:after{content:"";position:absolute;left:0;right:0;top:2px;border-top:1px solid var(--green)}
.m-hero{height:172px;color:#fff;text-align:center;padding-top:24px}
.m-hero h1{font-size:10.5px;font-weight:700;line-height:1.22;text-transform:uppercase;padding:0 18px}
.m-hero p{font-size:6px;margin:12px 0 20px}
.m-sec{padding:12px 9px 0}
.m-sec h2{font-size:7px}
.m-sec p.t{font-size:4.6px;line-height:1.65;text-align:center;margin:6px 0 8px}
.m-btn{font-size:5px;padding:4px 10px}
.m-cards{display:grid;grid-template-columns:1fr 1fr;gap:6px 6px;padding:0 8px;margin-top:14px}
.m-cards .img{height:107px}
.m-cards .label{font-size:5.3px;color:var(--blue);font-weight:700;margin-top:3px;text-transform:uppercase}
.m-process{height:260px;margin-top:14px}
.m-process .panel{position:absolute;inset:0;background:rgba(255,255,255,.7);padding:12px 15px}
.m-process h2{font-size:7px;color:var(--blue);font-weight:400}
.m-step{margin-top:12px}
.m-step .ic{width:11px;height:11px;background:var(--sky);margin-bottom:4px}
.m-step h4{font-size:6px;color:#2b95d2;font-weight:400}
.m-step p{font-size:4.7px;line-height:1.6;color:#555}
.m-why{height:245px;background:var(--pale);padding:15px 7px 0}
.m-why h2{font-size:7px;font-weight:400}
.m-wi{display:flex;gap:6px;margin-top:11px}
.m-wi .ic{width:14px;height:14px;border-radius:50%;background:var(--blue);flex:none}
.m-wi h4{font-size:5.2px;color:var(--blue);font-weight:400}
.m-wi p{font-size:4.4px;line-height:1.5;color:#555}
.m-grid{display:grid;grid-template-columns:1fr 1fr;grid-auto-rows:70px;gap:4px;padding:0 8px}
.m-stats{display:grid;grid-template-columns:1fr 1fr;gap:6px;padding:0 8px}
.m-stats .stat{height:86px}
.m-foot{height:28px;background:var(--green);color:#fff;font-size:4.6px;text-align:center;padding-top:11px;position:absolute;bottom:0;width:100%}
</style>
</head>
<body>

<div class="page desktop">
  <div class="d-top"><span>✉ info@ridgecrestbalusters.example</span><span>☎ (555) 014-2288</span></div>
  <div class="d-nav">
    <div class="brand"><span class="brand-mark"></span>RIDGECREST BALUSTERS</div>
    <ul><li>HOME</li><li>PRODUCTS</li><li>ABOUT</li><li>GALLERY</li><li>REMODEL PROJECTS</li><li><span class="btn">CONTACT</span></li></ul>
  </div>
  <div class="block d-hero photo" role="img" aria-label="Deck with black metal and glass railing overlooking a valley with pine trees">
    <h1>We believe that every outdoor space deserves the perfect blend of style, safety, and durability</h1>
    <p>Check out our best sellers</p>
    <span class="btn">Contact for free consultation
      <svg width="14" height="5" viewBox="0 0 14 5"><path d="M0 2.5h12M10 .5l2 2-2 2" stroke="#fff" fill="none" stroke-width=".8"/></svg></span>
    <div class="dots"><i></i><i></i><i></i><i></i></div>
  </div>
  <div class="block d-intro">
    <h2 class="title">We can help you find your perfect railing</h2>
    <p>At <b>Ridgecrest Balusters</b>, we believe that every outdoor space deserves the perfect blend of style, safety, and durability. Serving homeowners, builders, and commercial developers across the Washington State, we specialize in crafting custom railing systems designed to withstand the region's unique climate while enhancing the beauty of your outdoor living spaces.</p>
    <div class="btn-row"><span class="btn">About us →</span><span class="btn" style="background:#0094D4">Contact us →</span></div>
  </div>
  <div class="block d-products">
    <h2 class="title">Our products</h2>
    <p class="sub center">We offer a wide variety of custom and railing systems designed to meet the needs of every project</p>
    <div class="cards">
      <div class="card"><div class="img feature"><div class="inner"><b>Aluminum railings</b><p>For a sleek, low-maintenance option, our powder-coated aluminum railings provide strength, corrosion resistance, and a modern aesthetic. Available in a range of colors and finishes.</p><span class="more">Learn more</span></div></div><div class="label">Aluminum railings</div></div>
      <div class="card"><div class="img photo" role="img" aria-label="Glass panel railing on a balcony"></div><div class="label">Glass railings</div></div>
      <div class="card"><div class="img photo" role="img" aria-label="Cable railing around a patio with chairs" style="background:linear-gradient(160deg,#6d8ba5,#33404c)"></div><div class="label">Cable railings</div></div>
      <div class="card"><div class="img photo" role="img" aria-label="Custom stair railing on exterior steps"></div><div class="label">Custom</div></div>
    </div>
  </div>
  <div class="block d-process photo-light" role="img" aria-label="Multi-storey building with white balconies and black railings">
    <div class="panel">
      <h2 class="title" style="text-align:left">Our process</h2>
      <div class="step"><div class="ic"><svg width="8" height="8"><circle cx="4" cy="4" r="3" fill="none" stroke="#0094D4"/></svg></div><div><h4>Consultation &amp; Design</h4><p>We start by listening to your vision and understanding your specific needs. Our team will offer expert advice and design ideas to help you choose the best materials and styles.</p></div></div>
      <div class="step"><div class="ic"><svg width="8" height="8"><path d="M1 1l6 6M7 1L1 7" stroke="#0094D4"/></svg></div><div><h4>Professional Installation</h4><p>Our experienced team handles all aspects of installation, from measuring to securing, ensuring your railing is safe, secure, and perfectly aligned.</p></div></div>
      <div class="step"><div class="ic"><svg width="8" height="8"><path d="M1 4l2 2 4-5" stroke="#0094D4" fill="none"/></svg></div><div><h4>Ongoing Support</h4><p>We offer warranties on all of our products and services, and we are always available to help with maintenance or modifications down the road.</p></div></div>
    </div>
    <span class="btn">Contact for free consultation →</span>
  </div>
  <div class="block d-why">
    <h2 class="title">Why choose Ridgecrest Balusters</h2>
    <svg class="abs" style="left:170px;top:85px" width="160" height="160" viewBox="0 0 160 160">
      <path d="M10 20h35l18 30M150 20h-35l-18 30M10 140h35l18-30M150 140h-35l-18-30" stroke="#3c4650" stroke-width=".6" fill="none"/>
      <circle cx="80" cy="80" r="55" fill="#CADEEF"/>
      <circle cx="80" cy="80" r="47" fill="#fff" stroke="#0b6b38" stroke-width="3"/>
      <text x="80" y="84" text-anchor="middle" font-family="Lato,sans-serif" font-size="9" font-weight="700" fill="#0b6b38">RIDGECREST</text>
    </svg>
    <div class="why-item r" style="left:40px;top:95px"><h4>Locally Crafted<br>Regionally Resilient</h4><p>Our railings are designed with the Pacific Northwest's weather in mind—rain, snow, and everything in between. We use durable materials that are resistant to corrosion, moisture, and the elements, ensuring your railings stand the test of time.</p></div>
    <div class="why-ic" style="left:152px;top:97px"></div>
    <div class="why-item" style="left:363px;top:95px"><h4>Expert Installation &amp;<br>Craftsmanship</h4><p>Our skilled craftsmen take pride in delivering exceptional workmanship, while our professional installers ensure every railing is securely mounted and aligned to meet local safety codes.</p></div>
    <div class="why-ic" style="left:344px;top:97px"></div>
    <div class="why-item r" style="left:40px;top:195px"><h4>Custom Solutions for<br>Every Need</h4><p>We work closely with you to design and fabricate custom railing systems that perfectly suit your space, style, and functional requirements. From intricate designs to minimalistic finishes, we tailor every project to your vision.</p></div>
    <div class="why-ic" style="left:152px;top:197px;border-radius:2px"></div>
    <div class="why-item" style="left:363px;top:195px"><h4>Full-Service<br>Partner</h4><p>From the initial consultation and design process to installation and ongoing maintenance, we are with you every step of the way to ensure your project exceeds expectations.</p></div>
    <div class="why-ic" style="left:344px;top:197px"></div>
  </div>
  <div class="block d-show">
    <h2 class="title">Our complated project show case</h2>
    <div class="grid">
      <div class="feature"><div class="inner"><b>Valley View Custom Home; Cedar Falls, WA</b><p>Black aluminum horizontal railing</p><span class="more">Learn more</span></div></div>
      <div class="photo" role="img" aria-label="Deck with glass railing among trees"></div>
      <div class="photo" role="img" aria-label="Covered porch with black railing in winter" style="background:linear-gradient(160deg,#a5764d,#4a3c33)"></div>
      <div class="photo" role="img" aria-label="Exterior stairs with dark railing"></div>
      <div class="photo" role="img" aria-label="Deck with black picket railing"></div>
      <div class="photo-light" role="img" aria-label="Two-storey home with glass balcony railing"></div>
    </div>
    <div class="center" style="margin-top:14px"><span class="btn">View our all project →</span></div>
  </div>
  <div class="block d-test">
    <div class="abs photo" style="left:40px;top:0;width:107px;height:145px;background:linear-gradient(160deg,#88aacc,#2e3a44)" role="img" aria-label="Modern house with glass balcony railings"></div>
    <div class="abs photo" style="left:353px;top:0;width:107px;height:145px;background:linear-gradient(160deg,#c9a27d,#6c2634)" role="img" aria-label="Portrait of a smiling customer"></div>
    <div class="abs center" style="left:150px;width:200px;top:0">
      <h2 class="title">What people say about us</h2>
      <div style="font-size:26px;color:#555;margin-top:8px;line-height:1">“</div>
      <p style="font-size:5.3px;line-height:1.55">Lorem ipsum dolor sit amet, consectetur adipiscing elit, sed do eiusmod tempor incididunt ut labore et dolore magna aliqua. Quis ipsum suspendisse ultrices gravida.</p>
      <p style="font-size:7.5px;color:var(--blue);margin-top:10px">Maren Holt, WA</p>
      <p style="font-size:10px;color:var(--blue-dark);margin-top:14px;letter-spacing:2px">•••</p>
    </div>
  </div>
  <div class="block d-stats">
    <div class="stat"><div class="big">100+</div><small style="margin-top:6px">Over pros corporate<br>with any stuff</small><b>Professionals</b></div>
    <div class="stat"><small>Regular customers</small><div class="big" style="margin-top:6px">80%</div><small style="margin-top:4px">Clients with us<br>20 more years</small></div>
    <div class="stat"><small>Live time guarantee</small><svg width="30" height="34" viewBox="0 0 30 34" style="margin:3px 0"><circle cx="15" cy="13" r="11" fill="#0b6b38"/><path d="M8 22l-3 10 6-3 3 4 1-9M22 22l3 10-6-3-3 4" fill="#0b6b38"/></svg><small>We stand behind our<br>railing</small></div>
    <div class="stat"><small>Serving Washington<br>State</small><div role="img" aria-label="Map of Washington State regions" style="margin:4px auto 0;width:70px;height:50px;background:linear-gradient(120deg,#7b3f8f,#4db8a8 50%,#e5c23c)"></div></div>
  </div>
  <div class="d-foot">
    <div class="abs" style="left:40px;top:8px;width:38px;height:38px;background:#fff;color:var(--green);font-size:4.5px;font-weight:700;display:flex;align-items:center;justify-content:center;text-align:center">RIDGECREST<br>BALUSTERS</div>
    <div class="abs" style="left:40px;top:60px">Copyright © 2024 ridgecrestbalusters.</div>
    <div class="abs" style="left:213px;top:8px"><h5>LINK</h5><ul><li>Home</li><li>Products</li><li>About</li><li>Gallery</li><li>Remodel Projects</li></ul></div>
    <div class="abs" style="left:387px;top:8px;line-height:1.9"><h5>CONTACT</h5><p>⌖ 1420 Orchard Ln<br>&nbsp;&nbsp;&nbsp;Cedar Falls, WA 98000</p><p>☎ (555) 014-2288</p><p>✉ info@ridgecrestbalusters.example</p></div>
  </div>
</div>

<div class="page mobile">
  <div class="m-head"><div class="brand"><span class="brand-mark"></span>RIDGECREST BALUSTERS</div><div class="burger"></div></div>
  <div class="block m-hero photo" role="img" aria-label="Deck with black metal railing overlooking a valley">
    <h1>We believe that every outdoor space deserves the perfect blend of style, safety, and durability</h1>
    <p>CHECK OUT OUR BEST SELLERS</p>
    <span class="btn" style="font-size:5px;padding:5px 8px">Free consultation →</span>
  </div>
  <div class="m-sec">
    <h2 class="title" style="font-weight:400">We can help you find your perfect railing</h2>
    <p class="t">At <b>Ridgecrest Balusters</b>, we believe that every outdoor space deserves the perfect blend of style, safety, and durability. Serving homeowners, builders, and commercial developers across the Washington State, we specialize in crafting custom railing systems designed to withstand the region's unique climate while enhancing the beauty of your outdoor living spaces.</p>
    <div class="btn-row"><span class="btn m-btn">About us →</span><span class="btn m-btn" style="background:#0094D4">Contact us →</span></div>
    <h2 class="title" style="font-weight:400;margin-top:20px">Our products</h2>
    <p class="t">We offer a wide variety of custom and railing systems designed to meet the needs of every project</p>
  </div>
  <div class="m-cards">
    <div><div class="img feature"><div class="inner center"><b>Aluminum railings</b><p>For a sleek, low-maintenance option, our powder-coated aluminum railings provide strength, corrosion resistance, and a modern aesthetic. Available in a range of colors and finishes.</p><span class="more">Learn more</span></div></div><div class="label">Aluminum railings</div></div>
    <div><div class="img photo" role="img" aria-label="Glass panel railing on a balcony"></div><div class="label">Glass railings</div></div>
    <div><div class="img photo" role="img" aria-label="Cable railing around a patio" style="background:linear-gradient(160deg,#6d8ba5,#33404c)"></div><div class="label">Cable railings</div></div>
    <div><div class="img photo" role="img" aria-label="Custom stair railing"></div><div class="label">Custom</div></div>
  </div>
  <div class="block m-process photo-light" role="img" aria-label="Building with white balconies and black railings">
    <div class="panel">
      <h2 class="title" style="text-align:left">Our process</h2>
      <div class="m-step"><div class="ic"></div><h4>Consultation &amp; Design</h4><p>We start by listening to your vision and understanding your specific needs. Our team will offer expert advice and design ideas to help you choose the best materials and styles.</p></div>
      <div class="m-step"><div class="ic"></div><h4>Professional Installation</h4><p>Our experienced team handles all aspects of installation, from measuring to securing, ensuring your railing is safe, secure, and perfectly aligned.</p></div>
      <div class="m-step"><div class="ic"></div><h4>Ongoing Support</h4><p>We offer warranties on all of our products and services, and we are always available to help with maintenance or modifications down the road.</p></div>
      <span class="btn" style="font-size:5px;padding:4px 8px;margin-top:10px">Free consultation →</span>
    </div>
  </div>
  <div class="block m-why">
    <h2 class="title">Why choose Ridgecrest Balusters</h2>
    <div class="m-wi"><div class="ic"></div><div><h4>Locally Crafted Regionally Resilient</h4><p>Our railings are designed with the Pacific Northwest's weather in mind—rain, snow, and everything in between, ensuring your railings stand the test of time.</p></div></div>
    <div class="m-wi"><div class="ic" style="border-radius:2px"></div><div><h4>Custom Solutions for Every Need</h4><p>We work closely with you to design and fabricate custom railing systems that perfectly suit your space, style, and functional requirements.</p></div></div>
    <div class="m-wi"><div class="ic"></div><div><h4>Expert Installation &amp; Craftsmanship</h4><p>Our skilled craftsmen take pride in delivering exceptional workmanship, with railings securely mounted to meet local safety codes.</p></div></div>
    <div class="m-wi"><div class="ic"></div><div><h4>Full-Service Partner</h4><p>From the initial consultation to installation and ongoing maintenance, we are with you every step of the way.</p></div></div>
  </div>
  <div class="block" style="height:300px;padding-top:14px">
    <h2 class="title" style="font-size:7px;font-weight:400">Our complated project show case</h2>
    <div class="m-grid" style="margin-top:32px">
      <div class="feature"><div class="inner center" style="padding:6px 4px"><b>Valley View Custom Home; Cedar Falls, WA</b><p>Black aluminum horizontal railing</p><span class="more">Learn more</span></div></div>
      <div class="photo" role="img" aria-label="Deck with glass railing among trees"></div>
      <div class="photo" role="img" aria-label="Exterior stairs with dark railing"></div>
      <div class="photo" role="img" aria-label="Deck with black picket railing"></div>
      <div class="photo-light" role="img" aria-label="Home with glass balcony railing"></div>
      <div class="photo" role="img" aria-label="Covered porch with black railing" style="background:linear-gradient(160deg,#a5764d,#4a3c33)"></div>
    </div>
    <div class="center" style="margin-top:10px"><span class="btn m-btn">View all project →</span></div>
  </div>
  <div class="block photo-light center" style="height:142px;margin-top:8px;padding:10px 12px 0" role="img" aria-label="Modern house with glass balcony railings">
    <h2 class="title" style="font-size:6.5px;font-weight:400">What people say about us</h2>
    <div style="width:26px;height:26px;border-radius:50%;margin:6px auto 0;background:linear-gradient(160deg,#c9a27d,#6c2634)" role="img" aria-label="Customer portrait"></div>
    <p style="font-size:5px;color:var(--blue);margin-top:3px">Maren Holt, WA</p>
    <div style="font-size:16px;color:#555;line-height:1">“</div>
    <p style="font-size:4.6px;line-height:1.5;color:#444">Lorem ipsum dolor sit amet, consectetur adipiscing elit, sed do eiusmod tempor incididunt ut labore et dolore magna aliqua. Quis ipsum suspendisse ultrices gravida.</p>
    <p style="font-size:7px;color:var(--blue-dark);letter-spacing:2px">•••</p>
  </div>
  <div class="m-stats" style="margin-top:16px">
    <div class="stat"><div class="big" style="font-size:22px;margin-top:6px">100+</div><small style="margin-top:6px">Over pros corporate<br>with any stuff</small><b style="font-size:7px">Professionals</b></div>
    <div class="stat"><small>Regular customers</small><div class="big" style="font-size:22px;margin-top:8px">80%</div><small style="margin-top:6px">Clients with us<br>20 more years</small></div>
    <div class="stat"><small>Live time guarantee</small><svg width="28" height="32" viewBox="0 0 30 34" style="margin:6px 0 4px"><circle cx="15" cy="13" r="11" fill="#0b6b38"/><path d="M8 22l-3 10 6-3 3 4 1-9M22 22l3 10-6-3-3 4" fill="#0b6b38"/></svg><small>We stand behind our<br>railing</small></div>
    <div class="stat"><small>Serving Washington<br>State</small><div role="img" aria-label="Map of Washington State regions" style="margin:6px auto 0;width:66px;height:50px;background:linear-gradient(120deg,#7b3f8f,#4db8a8 50%,#e5c23c)"></div></div>
  </div>
  <div class="m-foot">Copyright © 2024 ridgecrestbalusters.</div>
</div>

</body>
</html>
```